Referral card and Flyer design

Please see attached example of Flyer and Referral Card. I would like a similar type flyer and card but nicer design. Industrial/retro Automtive type design.

Referral card should be size of regular business card.

Flyer should be 8X10" typical printer paper size.

Business Logo and Name should be changed from Vantorel to GearHollow LLC and on flyer please remove the last option where it says ( a Night out on us ) .

Change address on referral card to
GearHollow LLC
412 N Pellam Rd
Youngsville NC 27583
GearHollowHaul.example
Call or Text 919-555-0147

```html
<!DOCTYPE html>
<html lang="en">
<head>
<meta charset="utf-8">
<title>Customer Referral Card – GearHollow LLC</title>
<link rel="stylesheet" href="https://fonts.googleapis.com/css2?family=Poppins:wght@600&family=Lobster+Two:ital,wght@0,400;0,700;1,400;1,700&display=swap">
<style>
  :root {
    --navy: #2b3589;
    --ink: #2a2a2a;
    --rule: #666666;
    --paper: #ffffff;
    --sky-light: #b8dcff;
    --sky-deep: #7db4ff;
  }
  * { margin: 0; padding: 0; box-sizing: border-box; }
  html, body { width: 1200px; height: 983px; overflow: hidden; }
  body {
    position: relative;
    background: radial-gradient(ellipse at 45% 55%, var(--sky-light) 0%, #a3ceff 55%, var(--sky-deep) 100%);
    font-family: "Lobster Two", cursive;
  }
  .board-title, .board-size {
    position: absolute;
    left: 0; width: 100%;
    text-align: center;
    font-family: "Poppins", sans-serif;
    font-weight: 600;
    color: var(--ink);
    letter-spacing: 1.5px;
  }
  .board-title { top: 140px; font-size: 24px; }
  .board-size { top: 803px; font-size: 25px; }

  .referral-card {
    position: absolute;
    left: 139px; top: 228px;
    width: 923px; height: 527px;
    background: var(--paper);
    box-shadow: 0 6px 18px rgba(40, 70, 130, 0.35);
  }
  .card-header {
    position: absolute; left: 0; top: 0;
    width: 923px; height: 81px;
    background: var(--navy);
  }
  .card-title {
    position: absolute; left: 0; top: 14px; width: 100%;
    text-align: center;
    color: var(--paper);
    font-weight: 700;
    font-size: 44px;
  }
  .offer {
    position: absolute; left: 0; top: 132px; width: 100%;
    text-align: center;
    color: var(--navy);
    font-style: italic; font-weight: 700;
    font-size: 27px;
  }
  .field { position: absolute; display: flex; align-items: flex-end; right: 62px; }
  .field-label { font-weight: 700; font-size: 19px; color: var(--ink); white-space: nowrap; }
  .field-line { flex: 1; height: 2px; background: var(--rule); margin: 0 0 7px 9px; }
  .field-referrer { left: 75px; top: 225px; }
  .field-client { left: 53px; top: 277px; }

  .brand {
    position: absolute; left: 0; top: 360px; width: 100%;
    display: flex; justify-content: center; align-items: center; gap: 10px;
  }
  .brand-dot { width: 22px; height: 22px; border-radius: 50%; background: var(--navy); }
  .brand-name { font-weight: 700; font-size: 34px; color: var(--navy); }

  .contact {
    position: absolute; left: 0; top: 452px; width: 100%;
    text-align: center;
    color: var(--navy);
    font-style: italic; font-weight: 700;
    font-size: 22px; line-height: 27px;
  }
</style>
</head>
<body>
  <h1 class="board-title">REFERRAL CARD - MOCKUP 2</h1>

  <section class="referral-card">
    <div class="card-header"></div>
    <h2 class="card-title">Customer Referral Card</h2>

    <p class="offer">Present this card to receive $25.00 off your first visit with us.</p>

    <div class="field field-referrer">
      <span class="field-label">Referred By</span><span class="field-line"></span>
    </div>
    <div class="field field-client">
      <span class="field-label">New Client Name</span><span class="field-line"></span>
    </div>

    <div class="brand">
      <span class="brand-dot"></span>
      <span class="brand-name">GearHollow LLC</span>
    </div>

    <p class="contact">412 N Pellam Rd, Youngsville NC 27583 &nbsp;|&nbsp; Call or Text 919-555-0147<br>GearHollowHaul.example</p>
  </section>

  <p class="board-size">SIZE : 3.5IN X 2.0 IN (REGUALR BUSINESS CARD SIZE)</p>
</body>
</html>
```